Website design for an Online pastry shop

Website Name : www.lanternandplum.example

Description of the website and its target audience
We are a premium pastry company producing delicious cakes, macarons, cookies, gelato, and other sweet dessert. Our differentiation is that our products are freshly produced with premium quality imported ingredients and one bite into our products set us apart from other bakery shop. We online retail online so as to provide high quality products at a affordable cost. Our products has received raving reviews by many food enthusiast even the hard to please ones. The products contain more natural ingredients and we do not add preservatives. The return rates for our pastry is almost 80%. You only need to try once to be return customers. Our greatest challenge is getting customer to take the first bite. We are so sure of our products that we are going to give people free food tasting.

We are based in China but all our products are developed by award winning chefs from 5 stars hotel. The target customer is woman 16 to 40+ in china. Working class ladies and demand high quality products. A modern, sophisticated and minimalist website

This is a competitive market and image is crucial for such a food ‘conscious ’ orientated customer. They want to feel that they are buying from a reliable company that take great effort to ensure food cleaniness and safety yet affordable price. We make almost 98% of sub ingredients ourselves and we make it by hand.

Style/theme ideas for the web page design
I am looking for a elegant a little rustic, handmade feel yet sophisticated design - one that is easy to the eye yet functional and easy for the user to navigate through. Good play of fonts to give let it feel unique and customised. Black and white is our corporate colours. However, we do not want black background as it does not tease the taste bud. All our colours should come from our products. Customers should be very close to our products. They eat with their eyes first. Black and white is just accent.

Inspirational and competitors websites
http://www.47tart.example/ ( Key competitor )
I like the simple, clean look. The products are the key focus
https://www.pelvora.example/
clean, fresh and different. Attractive with purpose. Feminine
http://moatandwillow.example/
this has a great layout - lots of information and nicely presented. Very sweet and feminine
http://www.storeharbourly.example/
product features is the focus
http://www.janetobrill.example/store/
fun, feminine, rustic

Number of pages needed : 6 ( Uncoded PSD design only )
Page descriptions
Home Page - This page will show what makes our products stand out from the competitors and provide an introduction of who we are.
2nd page : Product catalogue
3nd page: Detail Product page with pictures and descriptions. Select products size and add to cart....
4rd page: Brand Story with pictures and descriptions.
5th page Contact Us : Here they can contact or schedule an appointment for free product tasting
6th page : Check out page

• Please see the project wire frame file " main page.png " or file number 70

```html
<!DOCTYPE html>
<html lang="en">
<head>
<meta charset="utf-8">
<title>Lantern &amp; Plum — Pastry Shop</title>
<link href="https://fonts.googleapis.com/css2?family=Open+Sans:ital,wght@0,300;0,400;0,600;1,300;1,400&display=swap" rel="stylesheet">
<style>
:root{
  --brown:#5a2f22;
  --brown-soft:#8a5a4a;
  --peach-title:#e59a7a;
  --cream:#ffffff;
  --lavender:#efeaf4;
  --teal:#8fcfc6;
  --orange:#f2a468;
  --green:#9bc877;
  --red:#e8614a;
  --blue:#79a8d1;
  --text:#6a5a5a;
  --muted:#8e8290;
  --pack-blue:#7b9bc4;
}
*{margin:0;padding:0;box-sizing:border-box}
html,body{width:1200px;height:3300px;overflow:hidden}
body{font-family:"Open Sans",Arial,sans-serif;color:var(--text);background:var(--cream);position:relative}
.abs{position:absolute}
.center{text-align:center}

/* header */
.site-header{position:absolute;left:0;top:0;width:1200px;height:60px;background:var(--cream);z-index:5}
.nav a{position:absolute;top:20px;font-size:14px;color:#3a2a26;text-decoration:none;font-weight:400;white-space:nowrap}
.brand{position:absolute;left:521px;top:-48px;width:158px;height:158px;border-radius:50%;background:var(--brown);z-index:6;
  display:flex;align-items:flex-end;justify-content:center;padding-bottom:30px}
.brand span{color:#fff;font-size:15px;font-weight:400;font-family:"Open Sans",Arial,sans-serif;white-space:nowrap}

/* hero */
.hero-photo{left:0;top:60px;width:1200px;height:526px;
  background:linear-gradient(100deg,#3b1c14 0%,#6b2a22 25%,#c9b29a 45%,#8a6b55 65%,#d9c5b0 85%,#b99a82 100%)}
.hero-title{left:620px;top:150px;width:475px;text-align:center;color:#fff;font-style:italic;font-weight:300;font-size:32px;line-height:42px}
.btn{position:absolute;display:block;text-align:center;color:#fff;font-size:14px;text-decoration:none;border-radius:3px}
.btn-tasting{left:782px;top:286px;width:180px;height:43px;line-height:43px;background:var(--orange);font-size:15px}

/* intro */
.intro-title{left:213px;top:660px;width:400px;font-size:40px;font-weight:300;color:var(--peach-title);line-height:52px}
.intro-title .dark{color:var(--brown-soft)}
.ornament{position:absolute}
.intro-copy{left:243px;top:806px;width:340px;font-size:12.5px;line-height:21px;color:var(--muted)}
.btn-catalogue{left:314px;top:938px;width:183px;height:44px;line-height:44px;background:var(--teal);color:#3f5a57;font-size:15px}
.collage-tile{position:absolute;border:5px solid #fff;box-shadow:0 2px 6px rgba(0,0,0,.18)}

/* macarons */
.macaron-photo-left{left:0;top:1078px;width:680px;height:302px;clip-path:polygon(0 0,100% 0,72% 100%,0 100%);
  background:linear-gradient(120deg,#3a2218,#6b4634 40%,#b98a78 60%,#5a3a2a)}
.macaron-photo-right{left:470px;top:1078px;width:730px;height:302px;clip-path:polygon(29% 0,100% 0,100% 100%,0 100%);
  background:linear-gradient(100deg,#d9cde0,#e9d6e2 40%,#c7d6ea 75%,#9dc1de)}
.macaron-divider{left:0;top:1078px;width:1200px;height:302px;pointer-events:none}
.macaron-title{left:645px;top:1128px;width:400px;font-size:40px;font-weight:300;color:#c07a8e;line-height:52px}
.macaron-copy{left:645px;top:1222px;width:400px;font-size:13.5px;line-height:24.5px;color:#3a2e36}

/* popular */
.popular{left:0;top:1380px;width:1200px;height:840px;background:var(--lavender)}
.popular-title{left:300px;top:1430px;width:600px;font-size:40px;font-weight:300;color:#8a6a6a;line-height:54px}
.popular-title .accent{color:var(--peach-title)}
.popular-sub{left:300px;top:1543px;width:600px;font-size:13px;color:var(--muted)}
.product-photo{position:absolute;width:293px;height:182px}
.product-name{position:absolute;width:293px;text-align:center;font-size:15px;color:#2a2226}
.btn-view-green{left:550px;top:2138px;width:103px;height:34px;line-height:34px;background:var(--green);font-size:12px}

/* ice cream */
.icecream{left:0;top:2220px;width:1200px;height:389px;background:linear-gradient(90deg,#f8ddd1,#f4ccbc)}
.icecream-photo{left:173px;top:2252px;width:440px;height:328px;
  background:linear-gradient(135deg,rgba(243,213,138,.85) 0%,rgba(242,150,135,.85) 50%,rgba(191,226,168,.85) 100%)}
.icecream-title{left:618px;top:2286px;width:400px;font-size:40px;font-weight:300;color:#7a5252;line-height:54px}
.icecream-title .accent{color:#e98770}
.icecream-copy{left:634px;top:2390px;width:450px;font-size:14px;line-height:22px;color:#5a4848}
.btn-view-red{left:766px;top:2515px;width:105px;height:34px;line-height:34px;background:var(--red);font-size:12px}

/* packaging */
.packaging{left:0;top:2609px;width:1200px;height:381px;background:var(--lavender)}
.packaging-title{left:378px;top:2638px;width:400px;font-size:40px;font-weight:300;color:var(--pack-blue);line-height:54px}
.packaging-copy{left:403px;top:2743px;width:410px;font-size:13px;line-height:21px;color:var(--muted)}
.pack-tile{position:absolute;border:4px solid #fff;box-shadow:0 2px 6px rgba(0,0,0,.2)}
.pack-can{left:837px;top:2672px;width:188px;height:244px;border-radius:8px 8px 12px 12px;background:linear-gradient(90deg,#111,#2b2b2b 50%,#111)}

/* footer */
.site-footer{left:0;top:2990px;width:1200px;height:310px;background:var(--blue);color:#fff}
.footer-heading{position:absolute;font-size:14px;font-weight:400}
.footer-list{position:absolute;list-style:none;font-size:13px;line-height:19.5px}
.footer-list li::before{content:"•";margin-right:6px}
.contact-item{position:absolute;font-size:13px;line-height:17px;display:flex;gap:14px}
.newsletter-note{left:622px;font-size:12px}
.newsletter-field{left:622px;width:196px;height:26px;background:rgba(255,255,255,.28);border-radius:2px;font-size:12px;line-height:26px;padding-left:10px;color:#e8f0f8}
.social-dot{position:absolute;width:14px;height:14px;border-radius:50%;background:#fff}
.copyright{left:199px;font-size:13px}
</style>
</head>
<body>

<header class="site-header">
  <nav class="nav">
    <a style="left:178px">Home</a>
    <a style="left:245px">Product Catalogue</a>
    <a style="left:398px">Product Details</a>
    <a style="left:700px">Story</a>
    <a style="left:768px">Contact Us</a>
    <a style="left:876px">Check Out</a>
  </nav>
</header>
<div class="brand"><span>Lantern &amp; Plum</span></div>

<section>
  <div class="abs hero-photo" role="img" aria-label="Cherry cheesecake on a white plate with a cup of tea on a checked tablecloth"></div>
  <h1 class="abs hero-title">More natural ingredients<br>and no preservatives</h1>
  <a class="btn btn-tasting">Free Food Tasting</a>
</section>

<section>
  <h2 class="abs intro-title center">Made For You<br><span class="dark">With Love</span></h2>
  <svg class="ornament" style="left:363px;top:773px" width="100" height="18" viewBox="0 0 100 18"><path d="M2 9 H38 M62 9 H98" stroke="#7a5a50" stroke-width="1.5" fill="none"/><circle cx="50" cy="9" r="5" stroke="#7a5a50" stroke-width="1.2" fill="none"/></svg>
  <p class="abs intro-copy center">Our products are freshly produced with premium quality imported ingredients and one bite into our products set us apart from other bakery shop.<br>May you enjoy a new culinary experience in<br>Lantern &amp; Plum</p>
  <a class="btn btn-catalogue">View Catalogue</a>

  <div class="collage-tile" style="left:627px;top:655px;width:124px;height:178px;background:linear-gradient(160deg,#e9b8a0,#c0643f)" role="img" aria-label="Cake slice with tea"></div>
  <div class="collage-tile" style="left:751px;top:672px;width:124px;height:175px;background:linear-gradient(160deg,#d8d0c8,#9a6848 60%,#2a1a14)" role="img" aria-label="Macaron tower"></div>
  <div class="collage-tile" style="left:875px;top:658px;width:128px;height:172px;background:linear-gradient(160deg,#e8dcd0,#5a2a26 60%,#a87a60)" role="img" aria-label="Berry layer cake"></div>
  <div class="collage-tile" style="left:630px;top:836px;width:125px;height:178px;background:linear-gradient(160deg,#7a8aa0,#f3e6c8 55%,#c89a60)" role="img" aria-label="Cream souffle"></div>
  <div class="collage-tile" style="left:763px;top:848px;width:120px;height:180px;background:linear-gradient(160deg,#5ab0c0,#3a2a4a 55%,#2a2240)" role="img" aria-label="Blueberry tart"></div>
  <div class="collage-tile" style="left:886px;top:840px;width:124px;height:175px;background:linear-gradient(160deg,#f0ece8,#c8a890 55%,#7a4a3a)" role="img" aria-label="Pastry chef decorating cakes"></div>
</section>

<section>
  <div class="abs macaron-photo-left" role="img" aria-label="Colourful macarons on a dark wooden table"></div>
  <div class="abs macaron-photo-right" role="img" aria-label="Softly blurred pastel macarons"></div>
  <svg class="abs macaron-divider" width="1200" height="302" viewBox="0 0 1200 302"><line x1="680" y1="0" x2="472" y2="302" stroke="#fff" stroke-width="6"/></svg>
  <h2 class="abs macaron-title center">Macarons</h2>
  <svg class="ornament" style="left:795px;top:1186px" width="100" height="18" viewBox="0 0 100 18"><path d="M2 9 H38 M62 9 H98" stroke="#4a3a40" stroke-width="1.5" fill="none"/><circle cx="50" cy="9" r="5" stroke="#4a3a40" stroke-width="1.2" fill="none"/></svg>
  <p class="abs macaron-copy center">We have developed a variety of characteristic flavors<br>to meet your unique taste<br>Faced with such a variety of choices ,<br>how can you not choose twelve kinds ,<br>to experience this unique sweet.</p>
</section>

<section>
  <div class="abs popular"></div>
  <h2 class="abs popular-title center"><span class="accent">Most</span> Popular Products</h2>
  <svg class="ornament" style="left:550px;top:1496px" width="100" height="18" viewBox="0 0 100 18"><path d="M2 9 H38 M62 9 H98" stroke="#7a6a70" stroke-width="1.5" fill="none"/><circle cx="50" cy="9" r="5" stroke="#7a6a70" stroke-width="1.2" fill="none"/></svg>
  <p class="abs popular-sub center">Our products contain more natural ingredients and we do not add preservatives.</p>

  <div class="product-photo" style="left:161px;top:1608px;background:linear-gradient(160deg,#f2e8e0,#4a2418 50%,#d8c0a8)" role="img" aria-label="Chocolate shaving cake slice"></div>
  <div class="product-photo" style="left:454px;top:1608px;background:linear-gradient(160deg,#f6e2d0,#f0a050 45%,#c87a80)" role="img" aria-label="Gelato scoops in cones"></div>
  <div class="product-photo" style="left:747px;top:1608px;background:linear-gradient(160deg,#3a2a22,#9aa088 50%,#5a4030)" role="img" aria-label="Macarons on wood"></div>
  <div class="product-name" style="left:161px;top:1809px">Cakes</div>
  <div class="product-name" style="left:454px;top:1809px">Gelatos</div>
  <div class="product-name" style="left:747px;top:1809px">Macarons</div>

  <div class="product-photo" style="left:161px;top:1872px;background:linear-gradient(160deg,#e8e4e0,#a81a22 45%,#f2d8a8)" role="img" aria-label="Cherry cheesecake"></div>
  <div class="product-photo" style="left:454px;top:1872px;background:linear-gradient(160deg,#a88868,#f4eee0 50%,#7a6a58)" role="img" aria-label="Cream souffle with tea"></div>
  <div class="product-photo" style="left:747px;top:1872px;background:linear-gradient(160deg,#d8a070,#f4f0ec 55%,#c8a888)" role="img" aria-label="Meringue pie"></div>
  <div class="product-name" style="left:161px;top:2075px">Cheesecakes</div>
  <div class="product-name" style="left:454px;top:2075px">Souffles</div>
  <div class="product-name" style="left:747px;top:2075px">Pies</div>

  <a class="btn btn-view-green">VIEW ALL</a>
</section>

<section>
  <div class="abs icecream"></div>
  <div class="abs icecream-photo" role="img" aria-label="Photo of vanilla, strawberry and pistachio ice cream scoops"></div>
  <h2 class="abs icecream-title center"><span class="accent">Ice</span> Cream</h2>
  <svg class="ornament" style="left:768px;top:2343px" width="100" height="18" viewBox="0 0 100 18"><path d="M2 9 H38 M62 9 H98" stroke="#7a5252" stroke-width="1.5" fill="none"/><circle cx="50" cy="9" r="5" stroke="#7a5252" stroke-width="1.2" fill="none"/></svg>
  <p class="abs icecream-copy">In Lantern &amp; Plum , we strictly follow the tradition of handmade<br>Italian ice cream production process, focusing on ice cream<br>flavor and texture. To this end , we selected only high - quality<br>raw materials.</p>
  <a class="btn btn-view-red">VIEW ALL</a>
</section>

<section>
  <div class="abs packaging"></div>
  <h2 class="abs packaging-title center">Packaging</h2>
  <svg class="ornament" style="left:528px;top:2710px" width="100" height="18" viewBox="0 0 100 18"><path d="M2 9 H38 M62 9 H98" stroke="#5a4a5a" stroke-width="1.5" fill="none"/><circle cx="50" cy="9" r="5" stroke="#5a4a5a" stroke-width="1.2" fill="none"/></svg>
  <p class="abs packaging-copy center">Our products include packed cans , cones , cookies and custom packaging boxes , for a variety of special occasions. Our endless pursuit , want all of our Lantern &amp; Plum products , can bring you a comprehensive and healthy gelato experience.</p>
  <div class="pack-tile" style="left:180px;top:2736px;width:170px;height:125px;background:linear-gradient(160deg,#e8dcc0,#3a3030 50%,#e89aa0)" role="img" aria-label="Gelato cups in packaging"></div>
  <div class="pack-tile" style="left:334px;top:2842px;width:170px;height:127px;background:linear-gradient(160deg,#5a2a1a,#8a4a30 50%,#3a1a10)" role="img" aria-label="Chocolate curls dessert"></div>
  <div class="abs pack-can" role="img" aria-label="Black gift tin with colourful drips"></div>
</section>

<footer class="abs site-footer">
  <h3 class="footer-heading" style="left:194px;top:56px">Popular Links</h3>
  <ul class="footer-list" style="left:199px;top:88px">
    <li>About Us</li><li>Products</li><li>Taste</li><li>Story</li><li>Contact Us</li>
  </ul>

  <h3 class="footer-heading" style="left:391px;top:56px">Contact Info</h3>
  <div class="contact-item" style="left:394px;top:92px">
    <svg width="14" height="14" viewBox="0 0 14 14"><path d="M1 7 L7 1.5 L13 7 M3 6 V13 H11 V6" stroke="#fff" stroke-width="1.6" fill="none"/></svg>
    <span>Lantern &amp; Plum<br>Unit 4, Meadow Lane<br>District, Harbour Quay<br>second floor , 12</span>
  </div>
  <div class="contact-item" style="left:394px;top:178px">
    <svg width="14" height="14" viewBox="0 0 14 14"><path d="M3 1 L5.5 3.5 L4 5.5 Q6 8.5 8.5 10 L10.5 8.5 L13 11 L11 13 Q5 12 1 3 Z" fill="#fff"/></svg>
    <span>020-55501482</span>
  </div>
  <div class="contact-item" style="left:394px;top:213px">
    <svg width="14" height="14" viewBox="0 0 14 14"><rect x="1" y="3" width="12" height="9" fill="#fff"/><path d="M1 3 L7 8 L13 3" stroke="#79a8d1" stroke-width="1.3" fill="none"/></svg>
    <span>info@lanternandplum.example</span>
  </div>

  <h3 class="footer-heading" style="left:624px;top:56px">Newsletter</h3>
  <div class="abs newsletter-note" style="top:93px">Subscribe to our newsletter</div>
  <div class="abs newsletter-field" style="top:115px">Email...</div>
  <svg class="abs" style="left:788px;top:123px" width="14" height="10" viewBox="0 0 14 10"><rect x="0.5" y="0.5" width="13" height="9" fill="none" stroke="#fff"/><path d="M0.5 0.5 L7 5.5 L13.5 0.5" stroke="#fff" fill="none"/></svg>

  <h3 class="footer-heading" style="left:871px;top:56px">Connect with Us</h3>
  <div class="social-dot" style="left:874px;top:105px"></div>
  <div class="social-dot" style="left:900px;top:105px"></div>
  <div class="social-dot" style="left:926px;top:105px"></div>
  <div class="social-dot" style="left:954px;top:105px"></div>

  <div class="abs copyright" style="top:255px">© Copyright information here</div>
</footer>

</body>
</html>
```